Computer Service Provider in Need of New Letterhead Design

We are Quarrybell Computer Services, a computer/IT services company that provides IT Support, software, hardware, virus monitoring, etc. in Vermont. We are looking for new letterhead, that is both professional and matches the current theme of our business cards & website.
Please note that we want to include the following information:
www.Quarrybell.example
802-555-0147
47 Fernhollow Road, Ashgrove, VT 05999
Reliable Support • Friendly Experts • Lasting Results
I will be attaching our logo along with the business card images.
We would love to have the

```html
<!DOCTYPE html>
<html lang="en">
<head>
<meta charset="utf-8">
<title>Quarrybell Computer Services – Letterhead</title>
<link href="https://fonts.googleapis.com/css2?family=Roboto:wght@400;500;700&family=Nunito+Sans:wght@400;600&display=swap" rel="stylesheet">
<style>
  :root {
    --backdrop: #e9e9e9;
    --paper: #ffffff;
    --brand-blue: #2a5a86;
    --accent-orange: #f0952a;
    --text-grey: #7a7a7a;
    --text-dark: #444444;
    --footer-text: #ffffff;
  }
  * { margin: 0; padding: 0; box-sizing: border-box; }
  html, body {
    width: 1200px;
    height: 866px;
    overflow: hidden;
    background: var(--backdrop);
  }
  .canvas { position: relative; width: 1200px; height: 866px; }
  .letterhead {
    position: absolute;
    left: 347px;
    top: 62px;
    width: 535px;
    height: 748px;
    background: var(--paper);
    font-family: "Roboto", Arial, sans-serif;
    color: var(--text-grey);
    overflow: hidden;
  }
  .brand {
    position: absolute;
    left: 47px;
    top: 48px;
    display: flex;
    align-items: center;
    gap: 8px;
  }
  .brand-mark { width: 41px; height: 41px; background: var(--brand-blue); flex: none; }
  .brand-name {
    font-weight: 700;
    font-size: 14px;
    line-height: 16px;
    color: var(--brand-blue);
    width: 140px;
  }
  .contact {
    position: absolute;
    left: 386px;
    top: 42px;
    font-family: "Nunito Sans", Arial, sans-serif;
    font-style: normal;
    font-size: 8.6px;
    line-height: 11px;
    color: var(--text-dark);
  }
  .contact-address { margin-bottom: 4px; }
  .contact-line { display: flex; align-items: center; gap: 5px; height: 12.5px; }
  .contact-line svg { width: 9px; height: 9px; flex: none; }
  .recipient {
    position: absolute;
    left: 47px;
    top: 213px;
    font-size: 10px;
    line-height: 14px;
  }
  .letter-body {
    position: absolute;
    left: 47px;
    top: 303px;
    width: 444px;
    font-size: 9.8px;
    line-height: 13.9px;
    text-align: justify;
  }
  .letter-body p + p { margin-top: 28px; }
  .signature {
    position: absolute;
    left: 47px;
    top: 502px;
    width: 101px;
    height: 68px;
    background: linear-gradient(135deg, #eef2f7, #dde6f0);
  }
  .signatory {
    position: absolute;
    left: 46px;
    top: 582px;
    font-size: 10px;
  }
  .footer-rule {
    position: absolute;
    left: 0;
    top: 713px;
    width: 100%;
    height: 3px;
    background: var(--accent-orange);
  }
  .footer-band {
    position: absolute;
    left: 0;
    top: 719px;
    width: 100%;
    height: 29px;
    background: var(--brand-blue);
    color: var(--footer-text);
    font-family: "Nunito Sans", Arial, sans-serif;
    font-size: 9.6px;
    display: flex;
    align-items: center;
    justify-content: center;
  }
</style>
</head>
<body>
<main class="canvas">
  <article class="letterhead">
    <header>
      <div class="brand">
        <div class="brand-mark"></div>
        <div class="brand-name">Quarrybell Computer Services</div>
      </div>
      <address class="contact">
        <div class="contact-address">47 Fernhollow Road<br>Ashgrove, VT 05999</div>
        <div class="contact-line">
          <svg viewBox="0 0 10 10" aria-hidden="true">
            <circle cx="5" cy="5" r="5" fill="var(--brand-blue)"/>
            <path d="M3.3 2.6 L4.2 2.4 L4.7 3.7 L4.1 4.2 Q4.6 5.4 5.8 5.9 L6.3 5.3 L7.6 5.8 L7.4 6.7 Q5.4 7.2 3.9 5.7 Q2.8 4.4 3.3 2.6 Z" fill="#fff"/>
          </svg>
          <span>802-555-0147</span>
        </div>
        <div class="contact-line">
          <svg viewBox="0 0 10 10" aria-hidden="true">
            <circle cx="5" cy="5" r="4.4" fill="none" stroke="var(--brand-blue)" stroke-width="0.9"/>
            <ellipse cx="5" cy="5" rx="1.9" ry="4.4" fill="none" stroke="var(--brand-blue)" stroke-width="0.7"/>
            <path d="M0.8 3.5 H9.2 M0.8 6.5 H9.2" stroke="var(--brand-blue)" stroke-width="0.7"/>
          </svg>
          <span>www.Quarrybell.example</span>
        </div>
      </address>
    </header>

    <div class="recipient">
      Dear Halvorsen<br>
      Tenbridge Graphic Corporation<br>
      Department Design
    </div>

    <section class="letter-body">
      <p>Lorem ipsum dolor sit amet, consectetuer adipiscing elit. Aenean commodo ligula eget dolor. Aenean massa. Cum sociis natoque penatibus et magnis dis parturient montes, nascetur ridiculus mus. Donec quam felis, ultricies nec, pellentesque eu, pretium quis, sem. Nulla consequat massa quis enim. Donec pede justo, fringilla vel, aliquet nec, vulputate eget, arcu. In enim justo, rhoncus ut, imperdiet a, venenatis vitae, justo. Nullam dictum felis eu pede mollis pretium. Integer tincidunt. Cras dapibus. Vivamus elementum semper nisi.Nullam dictum felis eu pede mollis pretium. Integer tincidunt. Cras dapibus. Vivamus elementum semper nisi.felis eu pede mollis pretium. Integer tincidunt. Cras dapibus.</p>
      <p>Quisque rutrum. Aenean imperdiet. Etiam ultricies nisi vel augue. Curabitur ullamcorper ultricies nisi. Nam eget dui. Etiam rhoncus. Maecenas tempus, tellus eget condimentum rhoncus, sem quam semper libero, sit amet adipiscing sem neque sed ipsum.felis pede mollis pretium. I am tincidunt. Cras dapibus.</p>
    </section>

    <div class="signature" role="img" aria-label="Handwritten signature of the director in blue ink"></div>
    <div class="signatory">Director/Excecutive Director</div>

    <footer>
      <div class="footer-rule"></div>
      <div class="footer-band">Reliable Support • Friendly Experts • Lasting Results</div>
    </footer>
  </article>
</main>
</body>
</html>
```